R.T.Pell Logging Web design

Our website needs a redesign. We want it to appear professional and easy to navigate. We will be adding videos and pictures to the new website. We do not sell any products on our website. It should be designed for informational purposes. Our company performs timber harvesting and forest management services. Attached is our new company logo.

www.rtpelllogging-example.com if you want to see our current website.

Industry/Entity Type

Graphic Design

Coding

Coded - Design and coding required

```html
<!DOCTYPE html>
<html lang="en">
<head>
<meta charset="utf-8">
<title>R.T. Pell Logging Company</title>
<link href="https://fonts.googleapis.com/css2?family=Source+Sans+3:wght@300;400;600;700&display=swap" rel="stylesheet">
<style>
:root{
  --bark:#4a2612;
  --bark-dark:#3b1d0e;
  --amber:#e8a23a;
  --gold:#f2c15a;
  --button:#5a2a12;
  --text:#5b4a3e;
  --heading:#5a2a12;
  --white:#ffffff;
  --nav:#5a4a40;
}
*{margin:0;padding:0;box-sizing:border-box}
html,body{width:1200px;height:1142px;overflow:hidden;background:var(--white)}
body{position:relative;font-family:"Source Sans 3",sans-serif;font-weight:300;color:var(--text)}
.topbar{position:absolute;left:0;top:0;width:1200px;height:46px;background:var(--bark-dark)}
.office-hours{position:absolute;left:672px;top:13px;font-size:14px;color:#e9ddd0}
.phone-icon{position:absolute;left:846px;top:10px}
.phone-number{position:absolute;left:882px;top:6px;font-size:22px;font-weight:400;color:var(--gold)}
.header{position:absolute;left:0;top:46px;width:1200px;height:75px;background:var(--white)}
.brand{position:absolute;left:178px;top:12px;display:flex;align-items:center;gap:10px}
.brand-square{width:52px;height:44px;background:var(--amber);border-radius:4px}
.brand-name{font-size:30px;font-weight:700;color:var(--heading);line-height:0.95;letter-spacing:0.5px}
.brand-name small{display:block;font-size:16px;letter-spacing:2.5px}
.nav{position:absolute;right:179px;top:32px;display:flex;gap:49px;font-size:15px;font-weight:400;color:var(--nav)}
.nav .active{color:var(--amber);font-weight:600}
.hero{position:absolute;left:0;top:121px;width:1200px;height:404px;background:linear-gradient(90deg,#e8c27a 0%,#dba95a 35%,#b06a2c 65%,#6a3a1a 100%)}
.hero-text{position:absolute;left:179px;top:118px;color:#3a2416}
.hero-kicker{font-size:18px}
.hero-title{font-size:45px;font-weight:300;line-height:1.05;margin-top:2px}
.hero-sub{font-size:17px;line-height:20px;margin-top:6px}
.hero-buttons{position:absolute;left:179px;top:265px;display:flex;gap:12px}
.btn{width:149px;height:46px;background:var(--button);color:var(--white);font-size:14px;font-weight:400;display:flex;align-items:center;justify-content:center;border-radius:3px;box-shadow:0 3px 0 #2e1408}
.welcome{position:absolute;left:179px;top:574px;width:520px}
.welcome-title{font-size:19px;font-weight:400;color:var(--heading);letter-spacing:0.5px;margin-left:3px}
.welcome-title strong{font-weight:400;font-size:30px}
.welcome-body{margin-top:14px;font-size:14px;line-height:16.8px}
.welcome-call{margin-top:20px;font-size:19px;line-height:23px;color:var(--heading);margin-left:2px}
.video-card{position:absolute;left:731px;top:583px;width:290px;height:249px}
.video-head{height:43px;background:var(--bark);color:var(--white);display:flex;justify-content:space-between;align-items:center;padding:0 16px 0 20px}
.video-head h2{font-size:20px;font-weight:300}
.video-head a{font-size:11px;font-weight:600;color:var(--white);text-decoration:underline}
.video-still{position:relative;height:206px;background:linear-gradient(180deg,#8a7560 0%,#a07a56 55%,#7a5a3c 100%)}
.video-play{position:absolute;left:117px;top:76px}
.follow{position:absolute;left:0;top:895px;width:1200px;height:184px;background:radial-gradient(ellipse at center,#7a4a28 0%,#5a3118 70%,#4a2612 100%)}
.follow h2{position:absolute;width:100%;top:36px;text-align:center;font-size:20px;font-weight:300;color:var(--white)}
.social{position:absolute;left:420px;top:84px;display:flex;gap:29px}
.social span{width:69px;height:69px;border-radius:50%}
.social .s1{background:#3a8fd0}
.social .s2{background:#2f5fa0}
.social .s3{background:#c8423a}
.social .s4{background:#2a6a9e}
.footer{position:absolute;left:0;top:1079px;width:1200px;height:63px;background:var(--bark-dark);color:#e9ddd0;font-size:15px;display:flex;justify-content:center;align-items:center;gap:32px}
</style>
</head>
<body>
<div class="topbar">
  <span class="office-hours">Our office hours : 7am-8pm</span>
  <svg class="phone-icon" width="24" height="24" viewBox="0 0 24 24"><path d="M6 3l3 0 1.5 4-2 1.5c1 2.5 3 4.5 5.5 5.5l1.5-2 4 1.5 0 3c0 1-1 2-2 2C10 19 4 13 4 5c0-1 1-2 2-2z" fill="none" stroke="#f2c15a" stroke-width="1.8"/><path d="M14 4a6 6 0 0 1 6 6M14 7a3 3 0 0 1 3 3" fill="none" stroke="#f2c15a" stroke-width="1.6"/></svg>
  <span class="phone-number">(555) 204-7781</span>
</div>
<header class="header">
  <div class="brand">
    <span class="brand-square"></span>
    <span class="brand-name">R.T. PELL<small>LOGGING COMPANY</small></span>
  </div>
  <nav class="nav">
    <span class="active">HOME</span><span>SERVICES</span><span>ABOUT US</span><span>LOCATION</span><span>CONTACT US</span>
  </nav>
</header>
<section class="hero" role="img" aria-label="Logging truck loaded with timber driving on a dusty dirt road">
  <div class="hero-text">
    <p class="hero-kicker">We are always buying timber in southeast Texas.</p>
    <h1 class="hero-title">Call for a free estimate.</h1>
    <p class="hero-sub">If you have a timber exemption on your property, call us.<br>We can write timber management plans for you.</p>
  </div>
  <div class="hero-buttons"><span class="btn">REQUEST A QUOTE</span><span class="btn">CONTACT US</span></div>
</section>
<section class="welcome">
  <h2 class="welcome-title">WELCOME TO <strong>R.T. PELL</strong> LOGGING COMPANY</h2>
  <p class="welcome-body">Receive high-quality professional logging and land clearing services, from R.T. Pell Logging Company based in Pine Hollow, TX. Whether your tract is large or small, our team of experts can provide the resources and solutions you need to get the job done right. Our track record for consistency, timely service, and expertise will continue to keep us competitive in the East Texas timber industry. We pay top dollar for your pine and hardwood timber.</p>
  <p class="welcome-call">To speak with an experienced member of staff, simply contact us 555-204-7781 at your earliest convenience.</p>
</section>
<aside class="video-card">
  <div class="video-head"><h2>VIDEO</h2><a>VIEW ALL &nbsp;&gt;</a></div>
  <div class="video-still" role="img" aria-label="Stacks of cut logs in a forest clearing">
    <svg class="video-play" width="56" height="56" viewBox="0 0 56 56"><circle cx="28" cy="28" r="25" fill="none" stroke="#fff" stroke-width="5"/><path d="M22 17l15 11-15 11z" fill="#fff"/></svg>
  </div>
</aside>
<section class="follow" role="img" aria-label="Cross-sections of stacked cut logs">
  <h2>FOLLOW US</h2>
  <div class="social"><span class="s1"></span><span class="s2"></span><span class="s3"></span><span class="s4"></span></div>
</section>
<footer class="footer"><span>© 2014 R.T.PELL LOGGING</span><span>|</span><span>ALL RIGHTS RESERVED</span></footer>
</body>
</html>
```